Zielgruppe
Wir sind ein Hotelunternehmen und eröffnen einen neuen Standort mit einem Boutique-Hotel. Die Zielgruppe sind Hotelgäste.
Aufgabenstellung
Wir benötigen ein Plakat mit den Maßen 6x4 m (siehe Bild anbei) für unsseren neuen Standort.
Farben Schwarz Weiss
Das Haus wird noch komplett weiß eingekleidet für die spätere Enthüllung und dann kommt das Plakat drüber
TEXT:
Großes Logo Hotel
Wir machen Lustenau noch schöner
Hier entsteht unser Boutique Hotel
Aus der Firmengruppe der Tarvolenz (als Logo)
Bild von Lena Grubhofer mit dem untertext: Lena Grubhofer, Geschäftsführerin Business Hotel Grubhofer

```html
<!DOCTYPE html>
<html lang="de">
<head>
<meta charset="utf-8">
<title>Grubhofer Boutique Hotel – Plakat</title>
<link href="https://fonts.googleapis.com/css2?family=Oswald:wght@300;400;500;600&family=Montserrat:wght@600&display=swap" rel="stylesheet">
<style>
  :root {
    --page-bg: #e9ecee;
    --poster-white: #ffffff;
    --ink: #1d1d1b;
    --panel-black: #1e1e1c;
    --photo-light: #d9d9d6;
    --photo-dark: #3a3a38;
  }
  html, body {
    margin: 0;
    padding: 0;
    width: 1200px;
    height: 1200px;
    overflow: hidden;
    background: var(--page-bg);
  }
  .poster {
    position: absolute;
    left: 0;
    top: 200px;
    width: 1200px;
    height: 800px;
    background: var(--poster-white);
    overflow: hidden;
    color: var(--ink);
  }
  .poster-art {
    position: absolute;
    inset: 0;
  }
  .hotel-logo {
    position: absolute;
    left: 170px;
    top: 70px;
    width: 570px;
    text-align: center;
  }
  .hotel-logo__name {
    font-family: "Oswald", sans-serif;
    font-weight: 500;
    font-size: 150px;
    line-height: 1;
    letter-spacing: 2px;
    margin: 0;
  }
  .hotel-logo__type {
    font-family: "Montserrat", sans-serif;
    font-weight: 600;
    font-size: 40px;
    letter-spacing: 10px;
    margin: 48px 0 0 0;
    line-height: 1;
  }
  .manager {
    position: absolute;
    left: 57px;
    top: 432px;
  }
  .manager__name {
    font-family: "Oswald", sans-serif;
    font-weight: 600;
    font-size: 118px;
    line-height: 1;
    margin: 0;
    letter-spacing: -1px;
  }
  .manager__role {
    font-family: "Oswald", sans-serif;
    font-weight: 300;
    font-size: 27px;
    letter-spacing: 4px;
    margin: 10px 0 0 2px;
    line-height: 1;
  }
  .claims {
    list-style: none;
    margin: 24px 0 0 0;
    padding: 0;
    font-family: "Oswald", sans-serif;
    font-weight: 300;
    font-size: 36px;
    line-height: 52px;
  }
  .claims li::before {
    content: "•";
    margin-right: 6px;
  }
  .group-brand {
    margin: 14px 0 0 6px;
    font-family: "Oswald", sans-serif;
    font-weight: 600;
    font-size: 36px;
    line-height: 1;
  }
</style>
</head>
<body>
  <main class="poster">
    <svg class="poster-art" width="1200" height="800" viewBox="0 0 1200 800">
      <defs>
        <linearGradient id="portraitTone" x1="0" y1="0" x2="0" y2="1">
          <stop offset="0" stop-color="var(--photo-dark)"/>
          <stop offset="0.35" stop-color="var(--photo-light)"/>
          <stop offset="1" stop-color="#f4f4f2"/>
        </linearGradient>
      </defs>
      <path class="backdrop-curve" d="M910 0 H1200 V800 H850 V380 C850 230 865 80 910 0 Z" fill="var(--panel-black)"/>
      <path class="portrait-area" role="img" aria-label="Portraitfoto von Lena Grubhofer in weißer Bluse, Hand an der Hüfte"
            d="M900 70 C980 50 1060 70 1080 150 L1090 330 C1160 360 1180 420 1175 520 L1165 800 H760 L760 690 C700 640 650 560 700 470 C730 410 790 370 850 340 L850 150 C855 100 870 78 900 70 Z"
            fill="url(#portraitTone)"/>
    </svg>

    <div class="hotel-logo">
      <p class="hotel-logo__name">Grubhofer</p>
      <p class="hotel-logo__type">BOUTIQUE HOTEL</p>
    </div>

    <section class="manager">
      <h1 class="manager__name">LENA GRUBHOFER</h1>
      <p class="manager__role">GESCHÄFTSFÜHRERIN BUSINESS HOTEL GRUBHOFER</p>
      <ul class="claims">
        <li>Wir machen Lustenau noch schöner</li>
        <li>Hier entsteht unser Boutique Hotel</li>
      </ul>
      <p class="group-brand">Tarvolenz</p>
    </section>
  </main>
</body>
</html>
```